Design Packaging for Brisa Alta Coffee

Please look at website at www.brisaltacoffeeworks.example
Need packaging for new coffee company. The size is: 6 x 9 x 3"

```html
<!DOCTYPE html>
<html lang="en">
<head>
<meta charset="utf-8">
<title>Brisa Alta Coffee – Coca Beans Label</title>
<link href="https://fonts.googleapis.com/css2?family=Rye&display=swap" rel="stylesheet">
<style>
  :root {
    --backdrop: #4cc8f1;
    --label-bg: #ffffff;
    --ink-brown: #2f1b1d;
    --ink-olive: #4a4d3a;
    --brand: #8c6a3a;
    --rule: #3a2a2a;
    --art-light: #f1efee;
    --art-mid: #cfc9c7;
  }
  * { box-sizing: border-box; margin: 0; padding: 0; }
  html, body {
    width: 1200px; height: 866px; overflow: hidden;
    background: var(--backdrop);
  }
  .label {
    position: absolute; left: 340px; top: 43px;
    width: 520px; height: 780px;
    background: var(--label-bg);
    box-shadow: 6px 8px 14px rgba(0,0,0,0.35);
    font-family: "Rye", serif;
    color: var(--ink-brown);
  }
  .art {
    position: absolute; left: 0; width: 100%;
  }
  .art-top {
    top: 0; height: 165px;
    background: linear-gradient(180deg, var(--art-mid) 0%, var(--art-light) 70%, var(--label-bg) 100%);
  }
  .art-bottom {
    bottom: 0; height: 150px;
    background: linear-gradient(0deg, var(--art-mid) 0%, var(--art-light) 70%, var(--label-bg) 100%);
  }
  .content {
    position: absolute; left: 94px; top: 166px; width: 332px;
    text-align: center;
  }
  .claim {
    font-size: 19px; line-height: 26px; letter-spacing: 0.5px;
  }
  .brand {
    margin-top: 20px; height: 34px;
    display: flex; align-items: center; justify-content: center; gap: 10px;
    color: var(--brand); font-size: 21px; white-space: nowrap;
  }
  .brand-dot {
    width: 22px; height: 22px; border-radius: 50%; background: var(--ink-brown);
  }
  .rule { border-top: 2px solid var(--rule); }
  .rule-top { margin-top: 18px; }
  .subtitle {
    font-size: 27px; line-height: 50px; letter-spacing: 0.5px; white-space: nowrap;
  }
  .product { display: block; margin: 4px 0 6px; }
  .product text { font-family: "Rye", serif; fill: var(--ink-olive); }
  .attributes {
    display: flex; align-items: center; justify-content: space-between;
    height: 56px; font-size: 24px; letter-spacing: 3px; padding: 0 2px;
  }
  .attributes .divider { width: 2px; height: 40px; background: var(--rule); }
  .vegan { font-size: 26px; line-height: 40px; letter-spacing: 0.5px; }
</style>
</head>
<body>
  <main class="label">
    <div class="art art-top" role="img" aria-label="Engraved illustration of cacao pods and leaves"></div>

    <section class="content">
      <p class="claim">100% ORGANIC<br>FOOD HEALTHY</p>
      <div class="brand">
        <span class="brand-dot"></span>
        <span class="brand-name">BRISA ALTA COFFEE</span>
      </div>
      <div class="rule rule-top"></div>
      <p class="subtitle">PREMIUM QUALITY</p>
      <div class="rule"></div>
      <svg class="product" width="332" height="188" viewBox="0 0 332 188" aria-label="Coca Beans">
        <text x="0" y="82" font-size="96" textLength="332" lengthAdjust="spacingAndGlyphs">COCA</text>
        <text x="0" y="176" font-size="96" textLength="332" lengthAdjust="spacingAndGlyphs">BEANS</text>
      </svg>
      <div class="rule"></div>
      <div class="attributes">
        <span>ORGANIC</span>
        <span class="divider"></span>
        <span>FRESH</span>
      </div>
      <div class="rule"></div>
      <p class="vegan">100% VEGAN</p>
    </section>

    <div class="art art-bottom" role="img" aria-label="Engraved illustration of cacao pods and leaves"></div>
  </main>
</body>
</html>
```